Bref créative
Harbor Crest - Complete Printing Package
Business Cards, Stationary, Envelopes
Professional
Tomas Lendrakis
Registered Migration Agent
PO Box 5871
Canberra ACT 2600
tomas@harborcrest.com.au
www.harborcrest.com.au
Harbor Crest is company that provides migration services to people seeking to apply for a visa to come to Australia.
We would like a business card that stands out, something that resembles an Australian passport or an Australian Visa.
maybe the back of the business card to look like the front cover of a passport.
Harbor Crest - Company Logo (please use second blue color - PANTONE 273 C)
Agent Number Option 1 charcoal color - please display this on the business card somewhere.
Agent Number Option 2 sand color - please display this on the business card somewhere.
GAF Member Option 1 Black - please display this on the business card somewhere.
GAF Member Option 2 Blue - please display this on the business card somewhere.
GAF Member Option 3 Reverse Blue - please display this on the business card somewhere.

```html
<!DOCTYPE html>
<html lang="en">
<head>
<meta charset="utf-8">
<title>Harbor Crest – Business Card</title>
<link href="https://fonts.googleapis.com/css2?family=PT+Serif:ital,wght@0,400;0,700;1,400;1,700&display=swap" rel="stylesheet">
<style>
  :root {
    --backdrop: #e9e6e1;
    --card-white: #ffffff;
    --brand-blue: #2a76ae;
    --brand-blue-deep: #1f6597;
    --rule-grey: #c9ccd0;
    --text-light: #ffffff;
  }
  * { margin: 0; padding: 0; box-sizing: border-box; }
  html, body {
    width: 1200px; height: 780px; overflow: hidden;
    background: var(--backdrop);
    font-family: "PT Serif", Georgia, serif;
  }
  .canvas {
    width: 1200px; height: 780px;
    display: flex; align-items: center; justify-content: center;
  }
  .business-card {
    position: relative;
    width: 1000px; height: 556px;
    border-radius: 34px;
    overflow: hidden;
    background: var(--card-white);
    box-shadow: 0 10px 30px rgba(0,0,0,0.18);
  }
  .brand {
    position: absolute;
    top: 118px; left: 0; right: 0;
    display: flex; align-items: center; justify-content: center;
    gap: 26px;
  }
  .brand-dot {
    width: 112px; height: 112px; border-radius: 50%;
    background: var(--brand-blue);
    flex: none;
  }
  .brand-text { display: flex; flex-direction: column; align-items: center; }
  .brand-name {
    font-size: 68px; font-weight: 400; color: var(--brand-blue);
    letter-spacing: 1px; line-height: 1;
  }
  .brand-tagline {
    margin-top: 10px;
    display: flex; align-items: center; gap: 14px;
    font-size: 22px; letter-spacing: 3px; text-transform: uppercase;
    color: var(--brand-blue);
  }
  .brand-tagline::before, .brand-tagline::after {
    content: ""; width: 70px; height: 2px; background: var(--brand-blue);
  }
  .contact-band {
    position: absolute; left: 0; right: 0; bottom: 0;
    height: 230px;
    background: var(--brand-blue);
    border-top: 12px solid var(--rule-grey);
    color: var(--text-light);
  }
  .agent {
    position: absolute; right: 548px; top: 52px;
    text-align: right;
  }
  .agent-name { font-size: 30px; font-weight: 700; font-style: italic; }
  .agent-role { font-size: 22px; margin-top: 6px; }
  .divider {
    position: absolute; left: 476px; top: 30px;
    width: 2px; height: 150px; background: var(--text-light);
  }
  .details {
    position: absolute; left: 506px; top: 18px;
    font-size: 21px; line-height: 1.35;
  }
  .address { margin-bottom: 10px; }
  .contact-line { display: flex; align-items: center; gap: 12px; }
  .contact-line svg { width: 20px; height: 20px; flex: none; }
</style>
</head>
<body>
<main class="canvas">
  <article class="business-card">
    <header class="brand">
      <span class="brand-dot" aria-hidden="true"></span>
      <div class="brand-text">
        <span class="brand-name">HarborCrest</span>
        <span class="brand-tagline">Migration Services</span>
      </div>
    </header>

    <section class="contact-band">
      <div class="agent">
        <p class="agent-name">Tomas Lendrakis</p>
        <p class="agent-role">Registered Migration Agent</p>
      </div>
      <div class="divider" aria-hidden="true"></div>
      <div class="details">
        <p class="address">PO Box 5871<br>Canberra ACT 2600</p>
        <p class="contact-line">
          <svg viewBox="0 0 20 20" aria-hidden="true"><rect x="5" y="1" width="10" height="18" rx="2" fill="#fff"/><rect x="7" y="4" width="6" height="9" fill="#2a76ae"/></svg>
          +61 (0) 400 582 903
        </p>
        <p class="contact-line">
          <svg viewBox="0 0 20 20" aria-hidden="true"><circle cx="10" cy="10" r="9" fill="#fff"/><text x="10" y="14" font-size="12" text-anchor="middle" fill="#2a76ae" font-family="Arial, sans-serif">@</text></svg>
          tomas@harborcrest.com.au
        </p>
        <p class="contact-line">
          <svg viewBox="0 0 20 20" aria-hidden="true"><circle cx="10" cy="10" r="9" fill="#fff"/><circle cx="10" cy="10" r="6" fill="none" stroke="#2a76ae" stroke-width="1.4"/><path d="M4 10h12M10 4v12" stroke="#2a76ae" stroke-width="1.4"/></svg>
          www.harborcrest.com.au
        </p>
      </div>
    </section>
  </article>
</main>
</body>
</html>
```